Velvet Dare Age Verification Landing Page

To create a visually appealing design for the landing page of the adult game "Velvet Dare" that confirms the visitor's age.
The design should have a simple and visually appealing look that focuses on two buttons labeled "Yes" and "No". The purpose of the page is to confirm that the visitor is 18 years of age or older before accessing the game's content. Responsive design that works well on desktop and mobile devices. The final output should be delivered in PSD, AI, or Sketch format, along with any necessary images or assets.
I have also attached examples.

```html
<!DOCTYPE html>
<html lang="en">
<head>
<meta charset="UTF-8">
<title>Velvet Dare — Age Verification</title>
<link rel="stylesheet" href="https://fonts.googleapis.com/css2?family=Poppins:wght@400;700&display=swap">
<style>
  :root {
    --page-bg: #1c1c1c;
    --scene-dark: #121212;
    --scene-mid: #2e2d2c;
    --scene-red: #3a1416;
    --brand-purple: #9a62b3;
    --panel-bg: #0b0b0b;
    --panel-border: #6b3f7a;
    --banner-red: #7e0000;
    --banner-border: #f2d6d6;
    --figure-tone: #e9e4e4;
    --text-light: #ffffff;
    --yes-green: #3b9a34;
    --no-red: #d20000;
  }
  * { margin: 0; padding: 0; box-sizing: border-box; }
  html, body {
    width: 1200px;
    height: 2308px;
    overflow: hidden;
    background: var(--page-bg);
    font-family: "Poppins", sans-serif;
  }
  .age-gate {
    position: relative;
    width: 1200px;
    height: 2308px;
    overflow: hidden;
  }
  .backdrop-scene {
    position: absolute;
    inset: 0;
    background:
      radial-gradient(ellipse 420px 520px at 60px 1250px, var(--scene-red), transparent 70%),
      radial-gradient(ellipse 700px 500px at 700px 500px, #3a3736, transparent 75%),
      linear-gradient(180deg, var(--scene-dark) 0%, var(--scene-mid) 45%, #3b3a39 75%, #2a2a2a 100%);
  }
  .brand-mark {
    position: absolute;
    left: 0;
    top: 180px;
    width: 1200px;
    display: flex;
    justify-content: center;
    align-items: center;
    gap: 28px;
  }
  .brand-dot {
    width: 44px;
    height: 44px;
    border-radius: 50%;
    background: var(--brand-purple);
  }
  .brand-name {
    color: var(--brand-purple);
    font-weight: 400;
    font-size: 92px;
    line-height: 1;
  }
  .verify-panel {
    position: absolute;
    left: 83px;
    top: 988px;
    width: 1034px;
    height: 743px;
    background: var(--panel-bg);
    border: 3px dashed var(--panel-border);
  }
  .adults-banner {
    position: absolute;
    left: 132px;
    top: 99px;
    width: 770px;
    height: 316px;
    background: var(--banner-red);
    border: 3px dashed var(--banner-border);
  }
  .banner-figure {
    position: absolute;
    background: var(--figure-tone);
    border-radius: 40px 40px 8px 8px;
  }
  .banner-figure--left { left: 14px; top: 6px; width: 86px; height: 304px; }
  .banner-figure--right { left: 690px; top: 152px; width: 72px; height: 158px; }
  .banner-heading {
    position: absolute;
    left: 100px;
    right: 80px;
    top: 40px;
    text-align: center;
    color: var(--text-light);
    font-weight: 700;
    line-height: 1;
  }
  .banner-heading .line-main { display: block; font-size: 104px; letter-spacing: 2px; }
  .banner-heading .line-sub { display: block; font-size: 88px; margin-top: 6px; }
  .age-question {
    position: absolute;
    left: 0;
    right: 0;
    top: 447px;
    text-align: center;
    color: var(--text-light);
    font-size: 42px;
    font-weight: 400;
  }
  .answer-button {
    position: absolute;
    top: 583px;
    width: 321px;
    height: 67px;
    display: flex;
    align-items: center;
    justify-content: center;
    color: var(--text-light);
    font-size: 36px;
    font-weight: 400;
    text-decoration: none;
  }
  .answer-button--yes { left: 166px; background: var(--yes-green); }
  .answer-button--no { left: 547px; background: var(--no-red); }
</style>
</head>
<body>
  <main class="age-gate">
    <div class="backdrop-scene" role="img" aria-label="Dimly lit lounge scene with a lace bra draped over a dark chair, a glass of red wine and playing cards on a marble table"></div>

    <header class="brand-mark">
      <span class="brand-dot"></span>
      <span class="brand-name">Velvet Dare</span>
    </header>

    <section class="verify-panel" aria-label="Age verification">
      <div class="adults-banner">
        <div class="banner-figure banner-figure--left" role="img" aria-label="Standing woman silhouette"></div>
        <div class="banner-figure banner-figure--right" role="img" aria-label="Crouching woman silhouette"></div>
        <h1 class="banner-heading">
          <span class="line-main">ADULTS</span>
          <span class="line-sub">ONLY 18+</span>
        </h1>
      </div>
      <p class="age-question">Are you 18 years of age or older?</p>
      <a class="answer-button answer-button--yes" href="#enter">YES, i'm adult</a>
      <a class="answer-button answer-button--no" href="#leave">No, i'm under 18</a>
    </section>
  </main>
</body>
</html>
```